Instructions for nurses on how to give a report on each shift

I have a 2-page reference sheet that needs to be updated to look more aesthetically pleasing.

Target Market(s)

Healthcare, nurses

Industry/Entity Type

Healthcare

Font styles to use
Sans Serif

Requirements
Must have
• Please make sure it is easy to read, the content is well organized and has a flow to it. Please also pick colors that would coordinate with our website www.brivolen.org (so mainly navy and white or off-white with accent colors.) Please make sure to add accent colors to break up the content. The MORVY name and title at the top should remain on the page but I'm not married to the star or logo style. You can do what you think looks best there. Way at the bottom in fine print, I would like for you to add BRIVOLEN © 2019 All rights reserved.

```html
<!DOCTYPE html>
<html lang="en">
<head>
<meta charset="utf-8">
<title>Shift Report Reference – Step 5</title>
<link href="https://fonts.googleapis.com/css2?family=Roboto:wght@300;400;500;700&display=swap" rel="stylesheet">
<style>
  :root{
    --navy:#1f3b5e;
    --sky:#d3e8f4;
    --sky-mid:#a9d0e8;
    --teal:#3fa2c8;
    --sun:#f6e251;
    --sun-soft:#fbef96;
    --ink:#1c2a3a;
    --paper:#ffffff;
  }
  *{box-sizing:border-box;margin:0;padding:0}
  html,body{width:900px;height:1200px;overflow:hidden;background:var(--paper)}
  body{font-family:"Roboto",Arial,sans-serif;color:var(--ink);position:relative}
  .abs{position:absolute}

  .foliage{background:radial-gradient(ellipse at center,var(--sky-mid) 0%,var(--sky) 55%,rgba(211,232,244,0) 75%)}
  .foliage--left{left:0;top:0;width:170px;height:110px}
  .foliage--right{right:0;top:0;width:260px;height:170px}

  .step-badge{left:34px;top:22px;width:66px;height:66px;border-radius:50%;background:var(--navy);
    border:4px solid var(--teal);color:#fff;font:700 34px "Roboto",sans-serif;display:flex;align-items:center;justify-content:center}
  .question{left:120px;top:28px;width:440px;font-size:16px;line-height:1.4}

  .factor-panel{left:36px;top:114px;width:180px;height:318px;background:var(--navy);border-radius:0 0 28px 0;padding:14px 0 0 26px}
  .factor-panel li{list-style:none;color:#fff;font-size:16px;line-height:1.1;margin-bottom:20px}
  .factor-panel li.two-line{line-height:1.7}
  .panel-dot{width:32px;height:32px;border-radius:50%;background:var(--sky)}

  .answer-band{left:216px;top:124px;width:640px;height:18px;background:var(--sky)}
  .answer{left:226px;color:var(--navy)}
  .answer__word{font:400 40px "Roboto",sans-serif;line-height:1}
  .answer__quote{font-size:15px;line-height:1.35;margin-top:4px}
  .answer-lines{left:228px;top:330px;font-size:15px;color:var(--navy)}
  .answer-lines div{width:240px;border-bottom:1.5px solid var(--navy);height:40px;padding-top:14px}

  .motto-link{left:400px;top:306px;width:180px;height:2px;background:var(--sky-mid)}
  .motto{left:530px;top:206px;width:330px;height:330px;border-radius:50%;background:var(--sun);
    box-shadow:0 0 0 10px var(--sun-soft);display:flex;flex-direction:column;justify-content:center;padding-left:34px;color:var(--navy)}
  .motto__line{font-size:28px;line-height:1.05}
  .motto__big{font-size:44px;font-weight:500}
  .motto__well{font-size:66px;font-weight:300;line-height:1}

  .section-title{font:400 30px "Roboto",sans-serif;font-variant:small-caps;letter-spacing:1px;color:var(--navy);z-index:1}
  .title-dot{width:56px;height:56px;border-radius:50%;background:var(--sun-soft)}
  .list-box{background:var(--sky);border-radius:0 0 24px 0;padding:16px 10px 12px 18px}
  .list-box li{list-style:none;font-size:13px;line-height:1.55;padding-left:26px;position:relative;margin-bottom:3px}
  .list-box li::before{content:"";position:absolute;left:2px;top:5px;border-left:9px solid var(--navy);border-top:6px solid transparent;border-bottom:6px solid transparent}

  .tips{left:564px;top:536px;width:300px;height:614px;background:var(--navy);padding:30px 18px 0 22px;color:#fff}
  .tips__title{font:500 22px "Roboto",sans-serif;color:var(--sun);margin-bottom:22px}
  .tips li{list-style:none;font-size:13px;line-height:1.65;padding-left:24px;position:relative;margin-bottom:6px}
  .tips li::before{content:"";position:absolute;left:0;top:5px;border-left:9px solid var(--sun);border-top:6px solid transparent;border-bottom:6px solid transparent}

  .footer-band{left:36px;top:1166px;width:828px;height:16px;background:var(--sky)}
  .footer-note{right:42px;top:1168px;font-size:10px;color:var(--navy)}
</style>
</head>
<body>
  <div class="abs foliage foliage--left" role="img" aria-label="Light blue leaf decoration"></div>
  <div class="abs foliage foliage--right" role="img" aria-label="Light blue leaf decoration"></div>

  <div class="abs step-badge">5</div>
  <p class="abs question">Any concerns or barriers related to your<br>ability to perform your job effectively?</p>

  <div class="abs answer-band"></div>
  <ul class="abs factor-panel">
    <li>Supplies</li>
    <li>Acuity</li>
    <li class="two-line">Time<br>constraints</li>
    <li>Family<br><span style="display:inline-block;margin-top:18px">requests</span></li>
    <li>Environment</li>
  </ul>
  <div class="abs panel-dot" style="left:200px;top:110px"></div>
  <div class="abs panel-dot" style="left:200px;top:212px"></div>

  <div class="abs answer" style="top:114px">
    <div class="answer__word">NO</div>
    <p class="answer__quote">"I have no concerns or barriers<br>affecting my ability to perform my job"</p>
  </div>
  <div class="abs answer" style="top:222px">
    <div class="answer__word">YES</div>
    <p class="answer__quote">"My concerns affecting my ability<br>to perform my job include..."</p>
  </div>
  <div class="abs answer-lines">
    <div>1)</div><div>2)</div><div>3)</div>
  </div>

  <div class="abs motto-link"></div>
  <div class="abs motto">
    <div class="motto__line">When <span class="motto__big">I</span></div>
    <div class="motto__line">is replaced by <span class="motto__big">WE</span></div>
    <div class="motto__line" style="font-size:25px">even illness becomes</div>
    <div class="motto__well">wellness</div>
  </div>

  <div class="abs title-dot" style="left:36px;top:478px"></div>
  <h2 class="abs section-title" style="left:42px;top:490px">Objectives:</h2>
  <ul class="abs list-box" style="left:36px;top:534px;width:246px;height:272px">
    <li>Accountability:<br>Declare roles and assignments</li>
    <li>Advocacy:<br>Identify patient needs</li>
    <li>Critical Thinking:<br>Prioritize and recognize obstacles</li>
    <li>Communication:<br>Share important information</li>
    <li>Collaboration:<br>Utilize an interdisciplinary approach</li>
  </ul>

  <div class="abs title-dot" style="left:36px;top:874px"></div>
  <h2 class="abs section-title" style="left:42px;top:886px">Outcomes:</h2>
  <ul class="abs list-box" style="left:36px;top:940px;width:246px;height:196px">
    <li>Share best practices</li>
    <li>Improve communication</li>
    <li>Promote cohesiveness</li>
    <li>Increase staff morale</li>
    <li>Enhance patient and organizational outcomes</li>
  </ul>

  <div class="abs title-dot" style="left:296px;top:478px"></div>
  <h2 class="abs section-title" style="left:302px;top:490px">Who:</h2>
  <ul class="abs list-box" style="left:296px;top:534px;width:248px;height:258px">
    <li>All nurses on the unit</li>
    <li>All nursing support staff (CNA/MA/HCT)</li>
    <li>Administrator</li>
    <li>Director of Nursing</li>
    <li>Head of pertinent disciplines (Dietary, Social Work, Physical Therapy, Engineering, Central Supply, etc.)</li>
  </ul>

  <div class="abs title-dot" style="left:296px;top:808px"></div>
  <h2 class="abs section-title" style="left:302px;top:820px">When:</h2>
  <ul class="abs list-box" style="left:296px;top:866px;width:248px;height:116px">
    <li>Every morning (assign a meeting time for each unit)</li>
    <li>Keep meetings within 15 minutes in length</li>
  </ul>

  <div class="abs title-dot" style="left:296px;top:1030px"></div>
  <h2 class="abs section-title" style="left:302px;top:1042px">Where:</h2>
  <ul class="abs list-box" style="left:296px;top:1086px;width:248px;height:52px;padding-top:14px">
    <li>Nursing station on each unit</li>
  </ul>

  <section class="abs tips">
    <h2 class="tips__title">HELPFUL TIPS:</h2>
    <ul>
      <li>Assign a meeting facilitator (usually the administrator of the facility)</li>
      <li>Standing during meetings keeps the meetings short and to the point</li>
      <li>Keeping meetings within 15 minutes emphasizes being prepared and direct</li>
      <li>Keep meeting times consistent (morning is best)</li>
      <li>Do not begin until everyone is present (minimizes stragglers</li>
      <li>Avoid discussing personnel concerns</li>
      <li>Include reminders for in-services, meetings, etc. and updates towards the end of the meeting</li>
      <li>Always conclude with achievements, milestones, praise, words of encouragement, motivational quote, etc.</li>
    </ul>
  </section>

  <div class="abs footer-band"></div>
  <p class="abs footer-note">BRIVOLEN © 2019 All rights reserved.</p>
</body>
</html>
```